Bus Card for Organic Hydroponic Produce company

We need a business card for a budding new business. We grow 100% organic, 100% hydroponic, 100% GMO free produce for sale in our local area. We need something bold and dynamic, not simple and elegant. We want to catch peoples attention and get them to visit our website to view more information about our products and services. Its difficult to explain on a business card the differences between our produce (tomatoes, cucumbers, peppers, etc...) and the kind they would buy at the local grocer or market. , so we need to push them to the website.
We have been brainstorming names for the company and have a few in mind, so choose whichever speaks most to your artistic flair and propose a card based on that one, or both. #1 "Marrowfield Organics" with a slogan something like....." When merely growing green merely isn't quite enough" OR #2 "Quillbrook Organics" with a slogan similar to...."The cutting edge in cleaner, purer organics" OR #3" "Tandrel Organics" with a slogan similar to: "Building a healthier future for those we leave behind"" OR #4 "Loamwise Path" with a slogan similar to: "Purity by Simplicity"
Eventually we will need assistance with web design, promotional and sales materials, etc. so if you offer those services, please indicate that with the design, though it is NOT necessary to offer any additional services to win this contest. WE will pick the winner solely on the business card we like the most.
We want something that stands out, and especially with the name "Oda's organics", we understand that a creative mind may wander into certain attention getting means that may not be quite within the realm of what we can hand out at our local grocer or farmers market. We definitely are not opposed to a little salacious undertone or allusion to attract attention, but please keep it tasteful if you skirt that grey area.
For our card, we use an online printer that can add foils, special die cuts, double sided cards, 3-d cards (we love these 32 pt cards), transparent or translucent cards and more. We love cards that have some of these things where possible and on all of our other business' cards we get rave reviews from customers about their uniqueness. plumtessa.com has the info on these accents if you wish to view what I am referencing.
So in conclusion, we want a unique, stylish, bold, vivid, 2 sided business card that will really stand out. Just usw a generic phone number and website for now and we will add them as they become available. Please email with any questions! Thanks in advance for your effort and creativity!
Target Market(s)
We are targeting parents who are conceintous of what their children and families are eating. Our target audience are moms, but we don't want to exclude anyone else who chooses to eat more healthy. Our target customer is the same customer that would shop at Brightcart stores or local farmers markets

```html
<!DOCTYPE html>
<html lang="en">
<head>
<meta charset="utf-8">
<title>Odas Organics – Business Card</title>
<link href="https://fonts.googleapis.com/css2?family=Federo&family=Alegreya+Sans:wght@400&family=Arvo&display=swap" rel="stylesheet">
<style>
  :root {
    --card-dark: #2f3837;
    --card-mid: #46504f;
    --silver: #aab6b5;
    --silver-soft: #9aa6a5;
    --divider: #8e9897;
  }
  * { margin: 0; padding: 0; box-sizing: border-box; }
  html, body { width: 1200px; height: 334px; overflow: hidden; background: var(--card-dark); }
  .spread { position: relative; width: 1200px; height: 334px; display: flex; }
  .card-face {
    position: relative; width: 600px; height: 334px; overflow: hidden;
    background:
      radial-gradient(ellipse 320px 120px at 30% 10%, rgba(110,125,123,.45), transparent 70%),
      radial-gradient(ellipse 260px 140px at 75% 85%, rgba(95,108,106,.35), transparent 70%),
      radial-gradient(ellipse 300px 160px at 50% 55%, rgba(30,38,37,.5), transparent 70%),
      linear-gradient(180deg, var(--card-mid), var(--card-dark));
  }
  .card-face + .card-face { border-left: 1px solid var(--divider); }

  .brand-name { font-family: "Federo", sans-serif; color: var(--silver); letter-spacing: .05em; text-transform: uppercase; white-space: nowrap; line-height: 1; font-weight: 400; }
  .tagline { font-family: "Alegreya Sans", sans-serif; color: var(--silver); white-space: nowrap; line-height: 1; }

  /* Front */
  .mark-slot { position: absolute; display: flex; align-items: center; gap: 10px; }
  .mark-dot { border-radius: 50%; background: var(--silver); flex: none; }
  .mark-label { font-family: "Federo", sans-serif; color: var(--silver); white-space: nowrap; }
  .front .mark-slot { left: 236px; top: 104px; }
  .front .mark-dot { width: 44px; height: 44px; }
  .front .mark-label { font-size: 17px; }
  .front .brand-name { position: absolute; left: 120px; top: 190px; font-size: 40px; }
  .front .tagline { position: absolute; left: 122px; top: 238px; font-size: 23px; }

  /* Back */
  .back .mark-slot { left: 40px; top: 90px; flex-direction: column; gap: 12px; }
  .back .mark-dot { width: 118px; height: 118px; opacity: .85; }
  .back .mark-label { font-size: 15px; }
  .back .brand-name { position: absolute; left: 276px; top: 77px; font-size: 30px; letter-spacing: .04em; }
  .back .tagline { position: absolute; left: 277px; top: 115px; font-size: 18px; }
  .back .rule { position: absolute; left: 276px; top: 142px; width: 297px; height: 1px; background: var(--divider); }
  .contact { position: absolute; left: 276px; top: 157px; font-family: "Arvo", serif; color: var(--silver-soft); }
  .address { font-size: 10px; line-height: 13px; margin-bottom: 9px; }
  .contact-line { display: flex; align-items: center; gap: 8px; font-size: 11px; height: 23px; }
  .contact-line svg { width: 12px; height: 12px; flex: none; fill: none; stroke: var(--silver-soft); stroke-width: 1.3; }
</style>
</head>
<body>
<div class="spread">
  <section class="card-face front">
    <div class="mark-slot">
      <span class="mark-dot"></span>
      <span class="mark-label">Odas Organics</span>
    </div>
    <h1 class="brand-name">Odas Organics</h1>
    <p class="tagline">As natural as if it were grown in eden</p>
  </section>

  <section class="card-face back">
    <div class="mark-slot">
      <span class="mark-dot"></span>
      <span class="mark-label">Odas Organics</span>
    </div>
    <h2 class="brand-name">Odas Organics</h2>
    <p class="tagline">As natural as if it were grown in eden</p>
    <div class="rule"></div>
    <div class="contact">
      <p class="address">48 Fernhollow Lane, Cedar Ridge,<br>VA 23999 Once we finalize everything</p>
      <p class="contact-line">
        <svg viewBox="0 0 12 12"><rect x="3" y="0.8" width="6" height="10.4" rx="1"/><line x1="5" y1="9.3" x2="7" y2="9.3"/></svg>
        555-555-5555
      </p>
      <p class="contact-line">
        <svg viewBox="0 0 12 12"><rect x="1" y="2.5" width="10" height="7"/><polyline points="1,2.5 6,6.5 11,2.5"/></svg>
        odasorganics@mailbay.com
      </p>
      <p class="contact-line">
        <svg viewBox="0 0 12 12"><circle cx="6" cy="6" r="5"/><ellipse cx="6" cy="6" rx="2.2" ry="5"/><line x1="1" y1="6" x2="11" y2="6"/></svg>
        www.OdasOrganics.com
      </p>
    </div>
  </section>
</div>
</body>
</html>
```